Harbor Dental New Patient Ad designed to catch a persons eye in a busy and cluttered newspaper

a minimalist newspaper ad to attract new patients to my office. i want an ad that is reminiscent of the Look Further Quince ads of 1998 or the 1960 Faltmobil "Turnip" ad. I would like the words Simply Bright in the middle of a blank space with the logo above, and the website and phone number with $88 new patient special info below it. The address need not be on the ad just that it is in North Haven.
i am trying to convey a modern office that does quality work with a vivid, colorful minimalist ad that catches the eye with its style and simplicity. Comparative ads in my area are very busy, generic, and homogenous.

Target Market(s)

Educated baby boomers
Health Conscious Millennials
Health Conscious Gen X

Font styles to use
Serif
Sans Serif

Colors
2369af
0493ce
00a990
abd037
fbed22
ffc214
f78f20

Requirements
Must have
• our logo
• our website
• our phone number
• $88 exam and cleaning
Nice to have
• a one word ad with one phrase in bold in the middle of blank space
• "Simply Bright"

```html
<!DOCTYPE html>
<html lang="en">
<head>
<meta charset="utf-8">
<title>Harbor Dental – Simply Bright</title>
<link href="https://fonts.googleapis.com/css2?family=Montserrat:wght@600;700;800&family=Open+Sans:wght@400;600&display=swap" rel="stylesheet">
<style>
  :root {
    --stage: #3a3a3a;
    --blue-deep: #1f5fae;
    --blue-mid: #2369af;
    --blue-bright: #0493ce;
    --orange: #f78f20;
    --white: #ffffff;
    --tooth-glow: #bfe6fb;
  }
  html, body {
    margin: 0;
    padding: 0;
    width: 1200px;
    height: 507px;
    overflow: hidden;
    background: var(--stage);
  }
  .ad {
    position: absolute;
    left: 437px;
    top: 23px;
    width: 326px;
    height: 461px;
    background:
      radial-gradient(ellipse 55% 30% at 50% 33%, rgba(4,147,206,0.9), rgba(4,147,206,0) 100%),
      linear-gradient(180deg, var(--blue-mid) 0%, #1c72c2 45%, var(--blue-deep) 100%);
    box-shadow: 0 2px 8px rgba(0,0,0,0.35);
    color: var(--white);
    text-align: center;
    font-family: "Montserrat", sans-serif;
  }
  .brand {
    position: absolute;
    top: 32px;
    left: 0;
    right: 0;
  }
  .brand__name {
    font-family: "Montserrat", sans-serif;
    font-weight: 800;
    font-size: 23px;
    line-height: 1;
    color: var(--white);
  }
  .tooth-art {
    position: absolute;
    top: 110px;
    left: 88px;
    width: 150px;
    height: 82px;
  }
  .headline {
    position: absolute;
    top: 196px;
    left: 0;
    right: 0;
    margin: 0;
    font-weight: 800;
    font-size: 48px;
    line-height: 43px;
    letter-spacing: 0.5px;
  }
  .headline__accent { color: var(--orange); display: block; }
  .headline__main { color: var(--white); display: block; }
  .offer {
    position: absolute;
    top: 303px;
    left: 0;
    right: 0;
    margin: 0;
    font-weight: 800;
    font-size: 33px;
    line-height: 33px;
  }
  .offer__price { color: var(--white); display: block; }
  .offer__service { color: var(--orange); display: block; }
  .divider {
    position: absolute;
    top: 385px;
    left: 142px;
    width: 42px;
    height: 1px;
    background: var(--white);
  }
  .contact {
    position: absolute;
    top: 397px;
    left: 0;
    right: 0;
    font-family: "Open Sans", sans-serif;
    font-size: 10.5px;
    line-height: 14px;
  }
  .contact__label {
    font-family: "Montserrat", sans-serif;
    font-weight: 700;
    font-size: 9.5px;
    color: var(--orange);
    margin-bottom: 2px;
  }
  .contact__sep { color: var(--orange); margin: 0 8px; }
</style>
</head>
<body>
  <main class="ad">
    <header class="brand">
      <div class="brand__name">Harbor Dental</div>
    </header>

    <svg class="tooth-art" viewBox="0 0 150 82" role="img" aria-label="Glossy white tooth illustration with small sparkles on a soft blue glow">
      <defs>
        <radialGradient id="toothGlow" cx="50%" cy="50%" r="50%">
          <stop offset="0%" stop-color="#bfe6fb" stop-opacity="0.85"/>
          <stop offset="45%" stop-color="#e9f6ff" stop-opacity="0.5"/>
          <stop offset="100%" stop-color="#0493ce" stop-opacity="0"/>
        </radialGradient>
      </defs>
      <ellipse cx="75" cy="41" rx="75" ry="41" fill="url(#toothGlow)"/>
    </svg>

    <h1 class="headline">
      <span class="headline__accent">SIMPLY</span>
      <span class="headline__main">BRIGHT</span>
    </h1>

    <p class="offer">
      <span class="offer__price">$88 EXAM &amp;</span>
      <span class="offer__service">CLEANING</span>
    </p>

    <div class="divider"></div>

    <footer class="contact">
      <div class="contact__label">FOR MORE INFORMATION</div>
      <div class="contact__address">42 Quarry Lane Maple Hollow, CT 06490</div>
      <div class="contact__line">+0123 555 0188<span class="contact__sep">|</span>www.harbordental-mh.com</div>
    </footer>
  </main>
</body>
</html>
```